Mobile Optometry needs descriptive brochure and business cards for patients

I need a brochure design and business cards for a new optometry service that brings full ocular examination, refraction, and spectacle dispensing to the patient in need.
I will mainly be working out of senior homes so it needs to be very legible NO SMALL PRINT, CLEAR, CONSCIENCE.
The final design needs to incorporate the logo and colouring that was just selected from a previous project. I will add this file as soon as I get the final changes back from the designer.

Here is what I would like in the broacher. I don't have a fax number, website address, email address set up yet but have room for this.

Note: I have attached the logo I selected for the company. I may not have attached the most detailed version but this will give you an idea of colouring and style. I will upload the proper image soon.

Routine eye examinations are crucial for early detection of diseases of the eye and effects of systemic conditions for everybody. As we age we are at higher risk of vision loss due to Glaucoma, Age-related Macular Degeneration, Diabetic or Hypertensive Retinopathy, Cataracts and many other diseases.

During your complete ocular visual assessment you will be screened for all conditions that may be affecting you as well as treat any issues you may be suffering from. Common treatable complaints: Dry eyes, Watery eyes, Burning, Itching, Difficulty reading small print, Reduced distance vision, Glare, Light sensitiveness, and difficulty performing hobbies.

Here is what your complete examination includes

Step 1: Appointment Request
-Call
-Email
-Phone
-Fax

Step 2: Welcome form
-Patient Name, DOB, Veltmore Care Plan number
-List current medications, allergies
-Current Visual difficulties
-Previous spectacle prescription (if available)

Step 3: Ocular Visual Assessment and Discussion of Results
-History & Symptoms
-Refraction
-Dilation and thorough ocular/retinal screening
-Spectacle or magnifier dispense if required
-Ophthalmologist or medical practitioner referral if required

Step 4: Dispense and Delivery
-Return to fit custom made glasses
-Demonstrate use low vision device
-Discuss any questions/treatments/referrals
Updates

I have just increased the budget. I am running out of time and want some good designs. I want a modern, clean and clear product. Please submit, points for originality.

Target Market(s)

The target audience is Professionals, managers, senior care facilities, families. I want something clean and easy to read. I want something modern but not trendy and something that appeals to the masses.

Industry/Entity Type

Medical

Font styles to use
Sans Serif

Requirements
Must have
• easy to read
bright
professional
Contact information on the last page
Nice to have
• order of services layer out nicely. Try a version with clearly defined steps. Step 1. Step 2. Step 3. Could be multiple broachers that are packaged together.
Should not have
• cartoony
serif fonts (please use font that is in logo)

```html
<!DOCTYPE html>
<html lang="en">
<head>
<meta charset="utf-8">
<title>Mobile Optometry Brochure – Inside Spread</title>
<link href="https://fonts.googleapis.com/css2?family=Mulish:ital,wght@0,400;0,600;0,800;1,800&display=swap" rel="stylesheet">
<style>
  :root{
    --green:#8cc63f;
    --green-deep:#2e8b3e;
    --yellow:#eef06a;
    --yellow-soft:#f6f7a8;
    --paper:#fbfdf3;
    --stripe:#eef5dc;
    --ink:#222;
  }
  *{margin:0;padding:0;box-sizing:border-box}
  html,body{width:1200px;height:927px;overflow:hidden;background:#fff}
  body{font-family:"Mulish",sans-serif;color:var(--ink)}
  .spread{position:relative;width:1200px;height:927px;
    background:repeating-linear-gradient(90deg,var(--paper) 0 6px,var(--stripe) 6px 10px);}
  .waves{position:absolute;inset:0;width:1200px;height:927px}
  .fold{position:absolute;left:599px;top:0;width:2px;height:927px;background:rgba(255,255,255,.8)}
  .photo{position:absolute;border:2px solid #fff;box-shadow:0 1px 3px rgba(0,0,0,.2)}
  .photo-1{left:28px;top:114px;width:246px;height:171px;background:linear-gradient(120deg,#e8e4e0,#b9c4cc 55%,#6e86a6)}
  .photo-2{left:28px;top:312px;width:246px;height:118px;background:linear-gradient(90deg,#3a3434,#d8b8a4 55%,#efe3da)}
  .photo-3{left:24px;top:464px;width:246px;height:138px;background:linear-gradient(90deg,#cfc6bc,#e6d6c8 45%,#7d6a5e)}
  .photo-4{left:24px;top:622px;width:246px;height:164px;background:linear-gradient(90deg,#9fb8d2,#d9c3a6 50%,#e9e1d6)}
  .intro{position:absolute;left:294px;top:136px;width:270px;font-size:20px;line-height:25.5px;
    letter-spacing:.15px;text-align:justify;text-align-last:left;hyphens:manual;-webkit-hyphens:manual;word-spacing:-.5px}
  .intro p+p{margin-top:25px}
  .intro em{font-style:italic;font-weight:800;display:block;text-align:left}
  .steps{position:absolute;left:636px;top:146px;width:540px}
  .steps .lead{font-size:19px;margin-bottom:22px}
  .step h2{font-size:21px;font-weight:800;color:var(--green-deep);line-height:27px}
  .step h2 .cont{display:block;padding-left:75px}
  .step ul{list-style:none;font-size:17.5px;line-height:23.7px;margin-bottom:24px}
  .step li{padding-left:22px;position:relative}
  .step li::before{content:"•";position:absolute;left:7px}
  .step-1 ul{font-size:19px;line-height:25.5px;margin-bottom:22px}
  .step-2 ul{margin-bottom:36px}
</style>
</head>
<body>
<div class="spread">
  <svg class="waves" viewBox="0 0 1200 927" aria-hidden="true">
    <g id="topleft">
      <path d="M0,0 H600 V152 C470,50 250,28 0,84 Z" fill="var(--yellow)"/>
      <path d="M0,0 H600 V132 C470,40 250,18 0,70 Z" fill="var(--yellow-soft)"/>
      <path d="M0,0 H600 V112 C470,25 260,8 0,40 Z" fill="var(--green)"/>
    </g>
    <use href="#topleft" transform="translate(1200,0) scale(-1,1)"/>
    <g id="bottomleft">
      <path d="M0,760 C140,860 360,880 600,840 V927 H0 Z" fill="var(--yellow)"/>
      <path d="M0,785 C150,880 370,895 600,855 V927 H0 Z" fill="var(--yellow-soft)"/>
      <path d="M0,805 C160,900 380,905 600,870 V927 H0 Z" fill="var(--green)"/>
    </g>
    <use href="#bottomleft" transform="translate(1200,0) scale(-1,1)"/>
  </svg>
  <div class="fold"></div>

  <div class="photo photo-1" role="img" aria-label="Optometrist examining a senior man at a slit lamp"></div>
  <div class="photo photo-2" role="img" aria-label="Close view of an ophthalmoscope examining an older woman's eye"></div>
  <div class="photo photo-3" role="img" aria-label="Optometrist checking a senior woman's eyes at home"></div>
  <div class="photo photo-4" role="img" aria-label="Nurse speaking with a smiling senior woman"></div>

  <div class="intro">
    <p><em>Routine eye examinations</em> are crucial for early detection of diseases of the eye and effects of sys&shy;temic condi&shy;tions for every&shy;body. As we age we are at higher risk of vision loss due to Glau&shy;coma, Age-related Macular Degen&shy;eration, Diabetic or Hyper&shy;tensive Retin&shy;opathy, Cata&shy;racts and many other dis&shy;eases.</p>
    <p>During your complete ocular visual assess&shy;ment you will be screened for all con&shy;ditions that may be affecting you as well as treat any issues you may be suffer&shy;ing from. Common treat&shy;able com&shy;plaints: Dry eyes, Watery eyes, Burn&shy;ing, Itching, Diffi&shy;culty reading small print, Reduced dis&shy;tance vision, Glare, Light sensi&shy;tive&shy;ness, and diffi&shy;culty perform&shy;ing hob&shy;bies.</p>
  </div>

  <div class="steps">
    <p class="lead">Here is what your complete examination includes</p>
    <section class="step step-1">
      <h2>Step 1: Appointment Request</h2>
      <ul><li>Call</li><li>Email</li><li>Phone</li><li>Fax</li></ul>
    </section>
    <section class="step step-2">
      <h2>Step 2: Welcome Form</h2>
      <ul>
        <li>Patient Name, DOB, Veltmore Care Plan number</li>
        <li>List current medications, allergies</li>
        <li>Current Visual difficulties</li>
        <li>Previous spectacle prescription (if available)</li>
      </ul>
    </section>
    <section class="step step-3">
      <h2>Step 3: Ocular Visual Assessment and <span class="cont">Discussion of Results</span></h2>
      <ul>
        <li>History &amp; Symptoms</li>
        <li>Refraction</li>
        <li>Dilation and thorough ocular/retinal screening</li>
        <li>Spectacle or magnifier dispense if required</li>
        <li>Ophthalmologist or medical practitioner referral if required</li>
      </ul>
    </section>
    <section class="step step-4">
      <h2>Step 4: Dispense and Delivery</h2>
      <ul>
        <li>Return to fit custom made glasses</li>
        <li>Demonstrate use low vision device</li>
        <li>Discuss any questions/treatments/referrals</li>
      </ul>
    </section>
  </div>
</div>
</body>
</html>
```